Book cover for the book The Copper Lantern Beneath Harrow Lake

This is a 6x9 paperback book titled The Copper Lantern Beneath Harrow Lake: Field Notes on Tidal Rhythms from Sailors and Keepers Along the Northern Coast. It will be a cover full of love, reunion, and warmth. No ghosts, cemeteries, and so on. I'm open to any creative design. Might include someone rising in spirit from a sick bed to the welcoming arms of loved ones. Or someone being greeted by family in a scene of enchanting beauty that is the life after this life. The world of the life after this life is just like earth, except more beautiful, with colors we can't imagine, large flowers, opulent buildings, and people all young wearing robes of varying colors. No religious symbols. No sun, moon, or stars.

Font styles to use
Serif

Requirements
Should not have
• Cemeteries, ghosts, anything ghoulish and spooky

```html
<!DOCTYPE html>
<html lang="en">
<head>
<meta charset="utf-8">
<title>The Copper Lantern Beneath Harrow Lake — Cover</title>
<link rel="stylesheet" href="https://fonts.googleapis.com/css2?family=Bodoni+Moda:opsz,wght@6..96,400;6..96,500;6..96,700&display=swap">
<style>
  :root {
    --page: #ffffff;
    --sky-top: #3a0f2c;
    --sky-plum: #6c2457;
    --sky-rose: #d97c98;
    --sky-coral: #f2747d;
    --sky-amber: #f7952e;
    --sky-dusk: #5a1838;
    --ground: #000000;
    --ink-light: #ffffff;
  }
  * { margin: 0; padding: 0; box-sizing: border-box; }
  html, body {
    width: 825px; height: 1200px; overflow: hidden;
    background: var(--page);
  }
  .canvas { position: relative; width: 825px; height: 1200px; }
  .cover {
    position: absolute; left: 42px; top: 46px; width: 739px; height: 1108px;
    overflow: hidden;
    font-family: "Bodoni Moda", "Didot", serif;
    color: var(--ink-light);
    text-align: center;
  }
  .cover-art {
    position: absolute; inset: 0;
    background:
      radial-gradient(ellipse 45% 22% at 18% 78%, rgba(247,149,46,0.85), rgba(247,149,46,0) 70%),
      radial-gradient(ellipse 60% 30% at 55% 62%, rgba(245,120,125,0.8), rgba(245,120,125,0) 70%),
      radial-gradient(ellipse 40% 40% at 100% 85%, rgba(58,12,36,0.8), rgba(58,12,36,0) 70%),
      radial-gradient(ellipse 30% 40% at 0% 60%, rgba(90,24,70,0.7), rgba(90,24,70,0) 70%),
      linear-gradient(180deg, var(--sky-top) 0%, var(--sky-plum) 20%, #8a3a6e 35%, var(--sky-rose) 45%, var(--sky-coral) 62%, var(--sky-dusk) 88%, #3a0c22 95%);
  }
  .ground-band {
    position: absolute; left: 0; right: 0; top: 1006px; bottom: 0;
    background: var(--ground);
  }
  .subtitle {
    position: absolute; left: 30px; right: 30px; top: 84px;
    font-size: 31px; line-height: 49px; font-weight: 400; letter-spacing: 0.3px;
  }
  .title { position: absolute; left: 0; right: 0; top: 282px; }
  .title span { display: block; }
  .title-small { font-size: 38px; font-weight: 500; line-height: 1; }
  .title-the { margin-bottom: 6px; }
  .title-large { font-size: 84px; font-weight: 700; line-height: 1.05; letter-spacing: 1px; }
  .title-mid { margin-top: 32px; }
  .title-huge { font-size: 124px; font-weight: 400; line-height: 1.05; margin-top: 4px; }
  .author {
    position: absolute; left: 0; right: 0; top: 1038px;
    font-size: 40px; font-weight: 700; line-height: 1;
  }
</style>
</head>
<body>
<div class="canvas">
  <div class="cover">
    <div class="cover-art" role="img" aria-label="Silhouette of a woman in a flowing dress leaning back with arms outstretched against a purple, pink and orange sunset sky with clouds"></div>
    <div class="ground-band"></div>
    <p class="subtitle">Field Notes on Tidal Rhythms from Sailors and Keepers Along the Northern Coast</p>
    <h1 class="title">
      <span class="title-small title-the">The</span>
      <span class="title-large">Copper Lantern</span>
      <span class="title-small title-mid">beneath</span>
      <span class="title-huge">Harrow Lake</span>
    </h1>
    <p class="author">Author Name</p>
  </div>
</div>
</body>
</html>
```